Window Tinting Website Design

We are working with a Window Tinting company in California. They do commercial, residential, and automotive tint.

Some websites for inspiration:
https://www.velofilmz.com/
https://www.tkglossbay.com/
https://orbishadez.com/

Thank you for taking the time to consider designing a website for us. We are web developers based in Stockton, CA, USA. Most of our projects go through the same process. Understanding this process may help you win a project with us. We custom-code all of our websites in-house. We don’t have any requirements as to what tools you use for your design, but we ask that you follow these guidelines.

IMAGES:
If you use any images or icons in the design, we ask that you have a link to the asset so we can purchase the image/icon. Most of the designs we submit do not have the customer’s images on them unless they have some great images. Be creative; show us the feeling you are trying to portray with your image choices. Use any royalty-free site you choose. We subscribe to Brellix and mainly use their images, but we can purchase images outside of Brellix. PLEASE NOTE: we will not submit designs to clients with watermarks on the images.

FONTS:
We ask that you identify the fonts you’re using in the design. This can be done in a message if you want. We typically use Tarvo Fonts and Brellix Fonts.

CONTENT:
We're always open to different content and ideas. We often submit designs with stock images so the client can see our vision. We typically take pictures after the website launch to use their images with our vision. Lorem Ipsum is fine for paragraphs, but we ask that you make the Headers with correct English. We want to be able to show the vision and identify the sections of the website.

INSPIRATION:
We typically add a couple of links in the brief of websites we like to help you get started in your design.

REVISIONS:
We do not often ask for revisions of the designs unless we see something in the design that may not appeal to the client. If there are slight changes that we want to make, we do that in the development process.

FEEDBACK:
We rarely give feedback on designs during the design process. We are working on many website projects and do not have the time to provide feedback. We usually respond if your request is well thought out and asks specific questions, but a note asking “feedback, please” usually goes unanswered.

```html
<!DOCTYPE html>
<html lang="en">
<head>
<meta charset="utf-8">
<title>Solara Tint Co. — Window Tinting</title>
<link rel="stylesheet" href="https://fonts.googleapis.com/css2?family=Bebas+Neue&family=Poppins:wght@400;500;600&display=swap">
<style>
:root{
  --red:#c8102e;
  --steel:#4c6b8a;
  --ink:#0c0c0c;
  --charcoal:#3a3a3a;
  --paper:#ffffff;
  --mist:#eef0f2;
  --text:#222222;
  --head:"Bebas Neue", sans-serif;
  --body:"Poppins", sans-serif;
}
*{margin:0;padding:0;box-sizing:border-box}
html,body{width:1200px;height:4090px;overflow:hidden}
body{position:relative;background:var(--paper);font-family:var(--body);color:var(--text)}
.abs{position:absolute}
.photo{position:absolute}
.brand{position:absolute;display:flex;align-items:center;gap:10px;font-family:var(--head);color:var(--red);font-size:36px;letter-spacing:1px}
.brand-dot{width:26px;height:26px;border-radius:50%;background:var(--red)}
.label{position:absolute;font-family:var(--head);color:var(--steel);font-size:22px;letter-spacing:.5px}
.title{position:absolute;font-family:var(--head);color:var(--red);font-size:52px;line-height:60px;letter-spacing:.5px}
.nav{position:absolute;display:flex;gap:37px;font-size:14px}
.nav a{color:inherit;text-decoration:none}
.nav .on{color:var(--red);text-decoration:underline}
.social{display:flex;gap:14px;align-items:center}
.social span{width:14px;height:14px;border-radius:50%;background:#fff;opacity:.85}
.social span.on{background:var(--red);opacity:1;width:22px;height:22px}
.circle-btn{position:absolute;border-radius:50%;display:flex;align-items:center;justify-content:center}
/* hero */
.hero{position:absolute;left:0;top:0;width:1200px;height:556px;background:linear-gradient(110deg,#2a2d31 0%,#4a4d52 35%,#1c1d20 70%,#0e0f11 100%)}
.hero .shade{position:absolute;inset:0;background:rgba(0,0,0,.35)}
.hero-kicker{left:0;width:1200px;top:232px;text-align:center;color:#fff;font-size:21px;font-weight:500}
.hero-head{left:0;width:1200px;top:262px;text-align:center;color:#fff;font-family:var(--head);font-size:66px;letter-spacing:1px}
.btn{position:absolute;display:flex;align-items:center;justify-content:center;color:#fff;font-size:15px;font-weight:500}
/* sections */
.dark{position:absolute;left:0;width:1200px;background:var(--ink)}
.card-cap{position:absolute;left:0;right:0;bottom:0;height:70px;display:flex;align-items:flex-end;justify-content:center;padding-bottom:16px;font-family:var(--head);color:#fff;font-size:26px;letter-spacing:.5px}
.stat{position:absolute;display:flex;align-items:center;gap:14px}
.stat-icon{width:86px;height:86px;border-radius:50%;border:3px solid var(--red);background:#111;display:flex;align-items:center;justify-content:center}
.stat-num{font-size:32px;font-weight:600;color:var(--red);line-height:34px}
.stat-cap{font-family:var(--head);font-size:24px;color:var(--red)}
</style>
</head>
<body>

<!-- HERO -->
<section class="hero">
  <div class="photo" role="img" aria-label="Technician polishing a car window in a workshop" style="inset:0;background:linear-gradient(100deg,#3b3e43 0%,#55585d 30%,#26282b 60%,#121315 100%)"></div>
  <div class="shade"></div>
  <div class="brand" style="left:90px;top:60px">Solara Tint Co.<span class="brand-dot"></span></div>
  <div class="abs" style="left:820px;top:50px;display:flex;align-items:center;gap:14px;color:#fff;font-size:15px">
    <span style="width:28px;height:28px;border-radius:50%;background:var(--red);display:flex;align-items:center;justify-content:center">
      <svg width="14" height="14" viewBox="0 0 24 24"><path fill="#fff" d="M6.6 10.8a15 15 0 0 0 6.6 6.6l2.2-2.2c.3-.3.7-.4 1-.2 1.1.4 2.3.6 3.6.6.6 0 1 .4 1 1V20c0 .6-.4 1-1 1A17 17 0 0 1 3 4c0-.6.4-1 1-1h3.5c.6 0 1 .4 1 1 0 1.3.2 2.5.6 3.6.1.3 0 .7-.2 1z"/></svg>
    </span>
    <span>123-456-7890</span>
    <div class="social" style="margin-left:24px"><span></span><span class="on"></span><span></span><span></span></div>
  </div>
  <nav class="nav" style="left:608px;top:88px;color:#fff">
    <a class="on">Home</a><a>About Us</a><a>Services</a><a>Testimonials</a><a>Contact Us</a>
  </nav>
  <p class="abs hero-kicker">Modern Equipment</p>
  <h1 class="abs hero-head">QUALITY SERVICE FOR YOU</h1>
  <a class="btn" style="left:495px;top:355px;width:208px;height:35px;background:var(--red)">Get a Free Estimate</a>
</section>

<!-- WELCOME -->
<section class="abs" style="left:0;top:556px;width:1200px;height:522px;background:var(--paper)">
  <div class="abs" style="left:119px;top:80px;width:384px;height:361px;border:2px solid var(--steel);padding:4px">
    <div class="photo" role="img" aria-label="Detailer in red shirt polishing the front grille of a car" style="position:relative;width:100%;height:100%;background:linear-gradient(120deg,#b9bcc0,#7d8187 50%,#a33 85%)"></div>
  </div>
  <div class="label" style="left:584px;top:116px">WELCOME TO</div>
  <h2 class="title" style="left:584px;top:142px;font-size:46px">SOLARA TINT CO.</h2>
  <p class="abs" style="left:584px;top:202px;width:506px;font-size:13.5px;line-height:21px;color:#333">Lorem Ipsum is simply dummy text of the printing and typesetting industry. Lorem Ipsum has been the industry's standard dummy text ever since the 1500s, when an unknown printer took a galley of type and scrambled it to make a type specimen book. It has survived not only five centuries, but also the leap into electronic typesetting, remaining essentially unchanged.</p>
  <div class="circle-btn" style="left:583px;top:328px;width:72px;height:72px;border:1.5px dashed var(--red)">
    <svg width="22" height="14" viewBox="0 0 22 14"><path d="M1 7h19M14 1l6 6-6 6" fill="none" stroke="var(--red)" stroke-width="2"/></svg>
  </div>
</section>

<!-- SERVICES -->
<section class="dark" style="top:1078px;height:628px">
  <div class="label" style="left:87px;top:232px">OUR SERVICES</div>
  <h2 class="title" style="left:87px;top:264px">QUALITY SERVICING<br>OPPORTUNITY</h2>
  <div class="abs" style="left:587px;top:81px;width:292px;height:250px;border:3px solid var(--red);background:var(--red)">
    <div class="photo" role="img" aria-label="White commercial van parked by a building" style="left:4px;top:4px;right:4px;bottom:70px;background:linear-gradient(160deg,#9aa0a6,#e2e4e6 55%,#6c7075)"></div>
    <div class="card-cap" style="height:70px">COMMERCIAL</div>
  </div>
  <div class="abs" style="left:898px;top:108px;width:213px;height:196px;background:var(--steel)">
    <div class="photo" role="img" aria-label="Car with camouflage wrap in a garage" style="left:0;top:0;right:0;bottom:60px;background:linear-gradient(135deg,#3a3c40,#b5662e 50%,#2a2c30)"></div>
    <div class="card-cap" style="height:60px;padding-bottom:12px">RESIDENTIAL</div>
  </div>
  <div class="abs" style="left:759px;top:349px;width:246px;height:198px;background:var(--steel)">
    <div class="photo" role="img" aria-label="Gloved hands applying tint film to a car window" style="left:0;top:0;right:0;bottom:60px;background:linear-gradient(135deg,#2c2e31,#8d9196 55%,#5b5f64)"></div>
    <div class="card-cap" style="height:60px;padding-bottom:12px">AUTOMOTIVE TINT</div>
  </div>
</section>

<!-- TESTIMONIALS -->
<section class="abs" style="left:0;top:1706px;width:1200px;height:464px;background:linear-gradient(90deg,#f6f7f8 0%,#eceef0 50%,#dfe2e5 100%)">
  <div class="photo" role="img" aria-label="Faded photo of a car in the rain" style="left:560px;top:0;width:640px;height:464px;background:linear-gradient(100deg,rgba(200,204,208,0),rgba(180,185,190,.45))"></div>
  <svg class="abs" style="left:87px;top:116px" width="46" height="34" viewBox="0 0 46 34"><path fill="var(--red)" d="M0 34V18C0 8 5 2 14 0l2 4c-5 2-7 5-7 10h9v20zM26 34V18c0-10 5-16 14-18l2 4c-5 2-7 5-7 10h9v20z"/></svg>
  <div class="abs" style="left:162px;top:129px;font-size:14px;color:#222">May 15</div>
  <p class="abs" style="left:87px;top:178px;width:470px;font-size:16.5px;line-height:24px;color:#222">Lorem Ipsum is simply dummy text of the printing and typesetting industry. Lorem Ipsum has been the industry's standard dummy text ever since the 1500s, when an unknown type specimen book.</p>
  <div class="photo" role="img" aria-label="Client portrait" style="left:87px;top:291px;width:63px;height:63px;border-radius:50%;border:3px solid var(--red);background:linear-gradient(135deg,#9c8e85,#5c524c)"></div>
  <div class="abs" style="left:159px;top:306px;font-size:15px;color:var(--red)">Mara V.</div>
  <div class="abs" style="left:159px;top:326px;font-size:12px;color:#222">CEO, Lorem Ipsum</div>
  <div class="circle-btn" style="left:453px;top:307px;width:35px;height:35px;background:var(--steel)">
    <svg width="16" height="10" viewBox="0 0 16 10"><path d="M15 5H2M6 1 2 5l4 4" fill="none" stroke="#fff" stroke-width="1.5"/></svg>
  </div>
  <div class="circle-btn" style="left:494px;top:307px;width:35px;height:35px;background:var(--red)">
    <svg width="16" height="10" viewBox="0 0 16 10"><path d="M1 5h13M10 1l4 4-4 4" fill="none" stroke="#fff" stroke-width="1.5"/></svg>
  </div>
  <div class="label" style="left:716px;top:194px">WHAT PEOPLE SAY</div>
  <h2 class="title" style="left:716px;top:228px">CLIENT'S TALK</h2>
</section>

<!-- RECENT WORK -->
<section class="dark" style="top:2170px;height:1164px">
  <div class="label" style="left:87px;top:76px">OUR RECENT WORKS</div>
  <h2 class="title" style="left:87px;top:108px">OUR SPECIAL<br>WORKS SEE NOW</h2>
  <div class="abs" style="left:636px;top:80px;width:475px;height:316px;border:2px solid var(--red);padding:8px">
    <div class="photo" role="img" aria-label="Classic blue car with chrome headlights" style="position:relative;width:100%;height:100%;background:linear-gradient(120deg,#3a2e22,#2a7fc0 45%,#1d1d22)"></div>
    <div class="circle-btn" style="left:205px;top:126px;width:64px;height:64px;background:rgba(200,16,46,.9)">
      <svg width="26" height="26" viewBox="0 0 26 26" fill="none" stroke="#fff" stroke-width="1.5"><path d="M2 9V2h7M2 2l8 8M24 17v7h-7M24 24l-8-8M17 2h7v7M24 2l-8 8M9 24H2v-7M2 24l8-8"/></svg>
    </div>
  </div>
  <div class="photo" role="img" aria-label="Red sports car with blue headlights in smoke" style="left:87px;top:296px;width:475px;height:359px;background:linear-gradient(135deg,#4a4d52,#b0172a 50%,#1a1c20)"></div>
  <div class="photo" role="img" aria-label="Dark car with red striped wrap" style="left:636px;top:471px;width:475px;height:317px;background:linear-gradient(135deg,#2b2f35,#a3202a 45%,#0f1316 80%)"></div>
  <div class="photo" role="img" aria-label="Sports car with neon yellow and black wrap" style="left:87px;top:728px;width:475px;height:357px;background:linear-gradient(135deg,#5b5e62,#c8d82a 45%,#222 80%)"></div>
  <div class="circle-btn" style="left:677px;top:900px;width:72px;height:72px;border:1.5px dashed var(--steel)">
    <svg width="22" height="14" viewBox="0 0 22 14"><path d="M1 7h19M14 1l6 6-6 6" fill="none" stroke="var(--steel)" stroke-width="2"/></svg>
  </div>
</section>

<!-- WHY US -->
<section class="abs" style="left:0;top:3334px;width:1200px;height:403px;background:var(--paper)">
  <h2 class="title" style="left:0;width:1200px;top:70px;text-align:center">WHY US</h2>
  <div class="stat" style="left:120px;top:180px">
    <div class="stat-icon"><svg width="42" height="42" viewBox="0 0 42 42" fill="none" stroke="#fff" stroke-width="1.6"><circle cx="21" cy="20" r="9"/><path d="M15 28l-3 10 9-4 9 4-3-10"/><path d="M21 15l1.5 3 3.3.5-2.4 2.3.6 3.3-3-1.6-3 1.6.6-3.3-2.4-2.3 3.3-.5z"/></svg></div>
    <div><div class="stat-num">10+</div><div class="stat-cap">YEARS OF EXPERIENCE</div></div>
  </div>
  <div class="stat" style="left:481px;top:180px">
    <div class="stat-icon"><svg width="42" height="42" viewBox="0 0 42 42" fill="none" stroke="#fff" stroke-width="1.6"><rect x="8" y="6" width="26" height="30" rx="2"/><path d="M8 14h26M13 22h16M13 28h10"/></svg></div>
    <div><div class="stat-num">36,000+</div><div class="stat-cap">WINDOWS TINTED</div></div>
  </div>
  <div class="stat" style="left:798px;top:180px">
    <div class="stat-icon"><svg width="44" height="42" viewBox="0 0 44 42" fill="none" stroke="#fff" stroke-width="1.6"><path d="M5 28V18l5-8h24l5 8v10z"/><circle cx="13" cy="29" r="3"/><circle cx="31" cy="29" r="3"/><path d="M11 18h22"/></svg></div>
    <div><div class="stat-num">300+</div><div class="stat-cap">VEHICLES WRAPPED</div></div>
  </div>
</section>

<!-- CTA -->
<section class="abs" style="left:0;top:3737px;width:1200px;height:164px;background:var(--charcoal)">
  <h2 class="abs" style="left:186px;top:50px;font-family:var(--head);color:#fff;font-size:58px;letter-spacing:1px">TELL US ABOUT YOUR PROJECT</h2>
  <a class="btn" style="left:801px;top:64px;width:210px;height:36px;background:var(--steel)">Get a Free Estimate</a>
</section>

<!-- FOOTER -->
<footer class="abs" style="left:0;top:3901px;width:1200px;height:138px;background:var(--ink)">
  <div class="brand" style="left:90px;top:50px;font-size:30px">Solara Tint Co.<span class="brand-dot" style="width:20px;height:20px"></span></div>
  <nav class="nav" style="left:365px;top:66px;color:#fff;gap:36px">
    <a class="on">Home</a><a>About Us</a><a>Services</a><a>Testimonials</a><a>Contact Us</a>
  </nav>
  <div class="abs" style="left:925px;top:58px;display:flex;align-items:center;gap:10px;color:#fff;font-size:21px">
    <span style="width:32px;height:32px;border-radius:50%;background:var(--red);display:flex;align-items:center;justify-content:center">
      <svg width="16" height="16" viewBox="0 0 24 24"><path fill="#fff" d="M6.6 10.8a15 15 0 0 0 6.6 6.6l2.2-2.2c.3-.3.7-.4 1-.2 1.1.4 2.3.6 3.6.6.6 0 1 .4 1 1V20c0 .6-.4 1-1 1A17 17 0 0 1 3 4c0-.6.4-1 1-1h3.5c.6 0 1 .4 1 1 0 1.3.2 2.5.6 3.6.1.3 0 .7-.2 1z"/></svg>
    </span>123-456-7890
  </div>
</footer>
<div class="abs" style="left:0;top:4039px;width:1200px;height:51px;background:var(--red)">
  <div class="abs" style="left:87px;top:16px;color:#fff;font-size:13px">© 2023 Solara Tint Co.. All Right Reserved</div>
  <div class="social abs" style="left:990px;top:14px"><span></span><span class="on" style="background:var(--steel)"></span><span></span><span></span></div>
</div>

</body>
</html>
```